Brightfield Chiropractic Business Cards

Business cards with new logo design. Will upload copy of current card. We like the layout, but we need a new logo. Family, husband holding up baby toward sky, mom and other child standing next to him. We will probably want to include a catch phrase with logo. TBD

```html
<!DOCTYPE html>
<html lang="en">
<head>
<meta charset="utf-8">
<title>Brightfield Chiropractic Business Cards</title>
<link href="https://fonts.googleapis.com/css2?family=Montserrat:wght@600;700&family=Arimo:wght@400;700&display=swap" rel="stylesheet">
<style>
  :root {
    --bg: #2a2a2a;
    --card-dark: #0c0c0c;
    --card-light: #ffffff;
    --red: #d9262b;
    --blue: #1d4f86;
    --grey-text: #c9c9c9;
    --ink: #1e1e1e;
    --divider: #3a3a3a;
  }
  * { box-sizing: border-box; margin: 0; padding: 0; }
  html, body { width: 1200px; height: 900px; overflow: hidden; }
  body {
    background: var(--bg);
    display: flex;
    flex-direction: column;
    align-items: center;
    justify-content: center;
    gap: 40px;
    font-family: "Arimo", Arial, sans-serif;
  }
  .card {
    width: 660px;
    height: 377px;
    border-radius: 22px;
    position: relative;
    overflow: hidden;
    box-shadow: 0 10px 30px rgba(0,0,0,.45);
  }
  /* Front */
  .card-front { background: var(--card-dark); display: flex; align-items: center; }
  .brand {
    width: 300px;
    flex: none;
    padding-left: 36px;
    font-family: "Montserrat", sans-serif;
    font-weight: 700;
    color: var(--blue);
    font-size: 24px;
    line-height: 1.1;
    letter-spacing: 0.3px;
    text-transform: uppercase;
    display: flex;
    align-items: center;
    gap: 12px;
    white-space: nowrap;
  }
  .brand-dot { width: 16px; height: 16px; border-radius: 50%; background: var(--blue); flex: none; }
  .divider { width: 1px; height: 170px; background: var(--divider); margin: 0 24px 0 0; flex: none; }
  .details { color: var(--grey-text); padding-right: 20px; }
  .person-name {
    font-family: "Montserrat", sans-serif;
    font-weight: 700;
    color: var(--red);
    font-size: 20px;
    text-transform: uppercase;
    letter-spacing: 0.2px;
    white-space: nowrap;
  }
  .person-title { font-size: 19px; margin-top: 4px; white-space: nowrap; }
  .contact { list-style: none; margin-top: 30px; font-size: 19px; }
  .contact li { display: flex; align-items: center; gap: 10px; margin-bottom: 6px; white-space: nowrap; }
  .contact svg { width: 18px; height: 18px; flex: none; }
  /* Back */
  .card-back { background: var(--card-light); }
  .map-area {
    position: absolute;
    left: 250px; top: 30px;
    width: 300px; height: 200px;
    background: linear-gradient(135deg, #f4f4f4, #e4e6ea);
  }
  .address {
    position: absolute;
    right: 70px; top: 250px;
    text-align: right;
    font-size: 19px;
    line-height: 1.25;
    color: var(--ink);
    font-style: normal;
  }
  .address .street { color: var(--blue); }
  .label { color: var(--red); font-weight: 700; }
</style>
</head>
<body>
  <section class="card card-front">
    <div class="brand"><span class="brand-dot"></span><span>Brightfield<br>Chiropractic</span></div>
    <div class="divider"></div>
    <div class="details">
      <h1 class="person-name">Dr. Daniel R. Ashford</h1>
      <p class="person-title">Chiropractic Physician</p>
      <ul class="contact">
        <li>
          <svg viewBox="0 0 24 24" aria-hidden="true"><path fill="#d9262b" d="M6.6 10.8a15.2 15.2 0 0 0 6.6 6.6l2.2-2.2a1 1 0 0 1 1-.25 11.4 11.4 0 0 0 3.6.57 1 1 0 0 1 1 1V20a1 1 0 0 1-1 1A17 17 0 0 1 3 4a1 1 0 0 1 1-1h3.5a1 1 0 0 1 1 1c0 1.25.2 2.450.57 3.6a1 1 0 0 1-.25 1z"/></svg>
          503-555-0142
        </li>
        <li>
          <svg viewBox="0 0 24 24" aria-hidden="true"><g fill="none" stroke="#d9262b" stroke-width="2"><circle cx="12" cy="12" r="9"/><path d="M3 12h18M12 3c3 3 3 15 0 18M12 3c-3 3-3 15 0 18"/></g></svg>
          AshfordChiropractic.com
        </li>
      </ul>
    </div>
  </section>

  <section class="card card-back">
    <div class="map-area" role="img" aria-label="Street map showing the clinic location between nearby avenues and roads"></div>
    <address class="address">
      <div class="street">2840 SE Cedar Grove Commons Dr.</div>
      <div>Maple Hollow, Oregon 97099</div>
      <div><span class="label">PHONE:</span> 503-555-0142 &nbsp;<span class="label">FAX:</span> 503-555-0187</div>
    </address>
  </section>
</body>
</html>
```